Website Page Re-Design

I have 2 pages that need to be re-designed on my site. This is the site so you can take a look and get a feel for the layout etc, www.vortaplay.com
I have included screen shots of the individual pages I want redone as well as some examples from other sites for ideas.

Homepage Story, would like the redo sunday file, to be made stunning, only the content, picture and share buttons need be altered the, would like and emphasis on intergrating the share buttons, the story page starts here http://www.vortaplay.com/league/ball-hockey/mens/news-division/ so what is beingcreated is when the read more is clicked

Free Agent Forms:
Needs to be re-worked so that there isn't so much white space on the page.

Industry/Entity Type

News

Requirements
Must have
• share buttons to slick very well intergrated
Nice to have
• Share buttons to be top notch

```html
<!DOCTYPE html>
<html lang="en">
<head>
<meta charset="utf-8">
<title>Vortaplay — League News</title>
<link rel="stylesheet" href="https://fonts.googleapis.com/css2?family=Noto+Sans:ital,wght@0,400;0,700;1,400&display=swap">
<style>
  :root{
    --bg-green:#82b33e;
    --bg-light:#a6cc6a;
    --panel:#e7f2d7;
    --panel-edge:#c9dcae;
    --tab-yellow:#ffe373;
    --tab-line:#8a7a3a;
    --ink:#2b2b2b;
    --title:#555a4f;
    --cream:#fff6c8;
    --banner-dark:#5c8d22;
    --banner-light:#8cbf4a;
    --share:#4b67a1;
    --share-edge:#2d4577;
    --card:#f6fbef;
    --muted:#6c7462;
    --c-linkvale:#4b67a1;
    --c-chirp:#3aa0d8;
    --c-mail:#6f9a2f;
    --c-link:#555a4f;
  }
  *{box-sizing:border-box;margin:0;padding:0}
  html,body{width:1200px;height:810px;overflow:hidden}
  body{
    position:relative;
    font-family:"Noto Sans",Verdana,sans-serif;
    background:radial-gradient(ellipse 700px 520px at 50% 22%,var(--bg-light),var(--bg-green));
    color:var(--ink);
  }
  a{text-decoration:none}
  .brand{position:absolute;left:132px;top:20px;font-size:46px;font-weight:700;color:var(--cream);letter-spacing:-1px}
  .top-nav{
    position:absolute;left:656px;top:0;width:413px;height:27px;
    background:var(--tab-yellow);border-radius:0 0 8px 8px;
    display:flex;align-items:center;font-size:14px;
  }
  .top-nav a{color:#111;padding:0 16px;border-left:1px solid var(--tab-line);line-height:21px}
  .top-nav a:first-child{border-left:none;padding-left:26px;padding-right:18px}
  .main-nav{
    position:absolute;left:511px;top:39px;width:556px;height:52px;
    background:#111;border-radius:6px 20px 4px 16px;
    display:flex;align-items:center;padding-left:30px;font-size:15px;font-style:italic;
  }
  .main-nav a{color:#fff;text-decoration:underline;padding:0 12px;border-left:1px solid #777;line-height:16px}
  .main-nav a:first-child{border-left:none;padding-left:12px}
  .page{
    position:absolute;left:131px;top:103px;width:938px;height:653px;
    background:var(--panel);border-radius:10px;box-shadow:0 2px 4px rgba(0,0,0,.2);
  }
  .banner{
    position:absolute;left:16px;top:13px;width:908px;height:108px;border-radius:6px;overflow:hidden;
    background:linear-gradient(180deg,var(--banner-light),var(--banner-dark));
  }
  .banner-photo{
    position:absolute;left:18px;top:0;width:632px;height:108px;
    background:linear-gradient(90deg,#9c5b4a,#d9573e 30%,#efe9df 55%,#c94a30 75%,#a8bb8a);
    opacity:.85;
  }
  .follow{
    position:absolute;left:696px;top:23px;width:164px;height:63px;background:#050505;border-radius:6px;
    display:flex;align-items:center;padding-left:16px;gap:12px;color:#fff;font-size:16px;line-height:17px;
  }
  .follow .dot{width:30px;height:30px;background:#5b7bbf;border-radius:4px;flex:none}
  .story{
    position:absolute;left:16px;top:131px;width:911px;height:502px;
    border:1px solid var(--panel-edge);border-radius:6px;
  }
  .story h1{position:absolute;left:19px;top:12px;font-size:18px;font-weight:700;color:var(--title)}
  .story-photo{
    position:absolute;left:17px;top:48px;width:411px;height:277px;border:5px solid #fff;
    box-shadow:0 0 2px rgba(0,0,0,.25);
    background:linear-gradient(180deg,#3d6fb4 0%,#5c86c0 45%,#e8e8e4 60%,#cfd3cb 78%,#3f7a3d 100%);
  }

  .share-card{
    position:absolute;left:452px;top:48px;width:442px;height:277px;
    background:var(--card);border:1px solid var(--panel-edge);border-radius:8px;
    box-shadow:0 2px 6px rgba(60,90,20,.12);padding:20px 22px;
  }
  .share-card h2{font-size:15px;font-weight:700;color:var(--title);margin-bottom:14px;display:flex;align-items:center;gap:8px}
  .share-card h2 svg{flex:none}
  .share-list{list-style:none;display:grid;grid-template-columns:1fr 1fr;gap:10px}
  .share-item{
    display:flex;align-items:center;gap:10px;height:44px;padding:0 12px;
    background:#fff;border:1px solid #dbe6cb;border-radius:6px;
    font-size:13px;font-weight:700;color:var(--ink);
  }
  .share-item .mark{width:24px;height:24px;border-radius:50%;flex:none;display:flex;align-items:center;justify-content:center}
  .share-item.linkvale .mark{background:var(--c-linkvale)}
  .share-item.chirpline .mark{background:var(--c-chirp)}
  .share-item.email .mark{background:var(--c-mail)}
  .share-item.copy .mark{background:var(--c-link)}
  .share-foot{
    position:absolute;left:22px;right:22px;bottom:20px;
    display:flex;align-items:center;justify-content:space-between;
    border-top:1px solid #dbe6cb;padding-top:14px;
  }
  .share-foot span{font-size:12px;color:var(--muted)}
  .share{
    width:96px;height:37px;border-radius:4px;
    background:linear-gradient(180deg,#6680b8,var(--share));border:2px solid var(--share-edge);
    color:#fff;font-weight:700;font-size:18px;display:flex;align-items:center;justify-content:center;gap:6px;
  }

  .story p{
    position:absolute;left:19px;top:344px;width:882px;font-size:12.6px;line-height:18.5px;color:#333;
  }
  .story p strong{color:#222}
  .legal{position:absolute;left:134px;top:775px;font-size:11px;color:#fff;letter-spacing:.5px}
</style>
</head>
<body>
  <div class="brand">Vortaplay</div>

  <nav class="top-nav">
    <a href="#">Home</a><a href="#">About Us</a><a href="#">FAQS</a><a href="#">Contact Us</a><a href="#">Jobs</a>
  </nav>

  <nav class="main-nav">
    <a href="#">Leagues</a><a href="#">Schedules &amp; More</a><a href="#">Register</a><a href="#">Pay</a><a href="#">Forum</a><a href="#">Sponsors</a>
  </nav>

  <main class="page">
    <div class="banner">
      <div class="banner-photo" role="img" aria-label="Row of league players in team jerseys and helmets"></div>
      <a class="follow" href="#"><span class="dot"></span><span>Find Us On<br>Linkvale</span></a>
    </div>

    <article class="story">
      <h1>Test Home Page Banner</h1>
      <div class="story-photo" role="img" aria-label="Ball hockey team in matching charity shirts posing with a large cheque on the gym floor"></div>

      <aside class="share-card" aria-label="Share this story">
        <h2>
          <svg width="18" height="18" viewBox="0 0 18 18" aria-hidden="true"><path d="M10 3l6 5-6 5V10C6 10 3.5 11.5 2 15c.5-5 3-8 8-8.5z" fill="#6f9a2f"/></svg>
          Share this story
        </h2>
        <ul class="share-list">
          <li><a class="share-item linkvale" href="#"><span class="mark"></span>Linkvale</a></li>
          <li><a class="share-item chirpline" href="#"><span class="mark"></span>Chirpline</a></li>
          <li><a class="share-item email" href="#"><span class="mark"><svg width="12" height="9" viewBox="0 0 12 9" aria-hidden="true"><rect x=".5" y=".5" width="11" height="8" fill="none" stroke="#fff"/><path d="M.5 .5L6 5l5.5-4.5" fill="none" stroke="#fff"/></svg></span>Email</a></li>
          <li><a class="share-item copy" href="#"><span class="mark"><svg width="12" height="12" viewBox="0 0 12 12" aria-hidden="true"><path d="M5 7l2-2M4 5L2.5 6.5a2 2 0 003 3L7 8M8 7l1.5-1.5a2 2 0 00-3-3L5 4" fill="none" stroke="#fff" stroke-width="1.4" stroke-linecap="round"/></svg></span>Copy link</a></li>
        </ul>
        <div class="share-foot">
          <span>Tell your team about it</span>
          <a class="share" href="#">
            <svg width="14" height="14" viewBox="0 0 18 18" aria-hidden="true"><path d="M10 3l6 5-6 5V10C6 10 3.5 11.5 2 15c.5-5 3-8 8-8.5z" fill="#fff"/></svg>
            Share
          </a>
        </div>
      </aside>

      <p><strong>At Vortaplay, you can find a ball hockey league that fits into your schedule. We offer men’s competitive, co-ed, and pick-up games for men and women. Ball hockey leagues are available on</strong> multiple nights at various gyms inside our facility, with each game an hour in length. Simply choose an evening that best suits your busy schedule, and you will be part of a ball hockey league or pick-up game at Vortaplay. It is never too late to join a league;however, any player must play a minimum of 2 regular season games to be eligible for the playoffs. So sharpen those stick-handling skills, and find a league at Vortaplay today!</p>
    </article>
  </main>

  <footer class="legal">© 2011, VORTAPLAY. ALL RIGHTS RESERVED.</footer>
</body>
</html>
```